Web page design - online proposal

We have an feature in our CRM to produce online proposals but at the moment they look very boring and plain. We need fresh new exciting designs for them that look highly professional.
We will be choosing 5 designs to use as templates so our users can upload their logo, photos and select their colours so that it generates a professional looking proposal for them.

Here is a sample of one of the existing proposals. All the information that's in the proposal will be used:

https://www.quillbrookhomes.com.au/portal/proposal.aspx?id=2857&passcode=KQWRPZ42&preview=1

One suggestion is to include compelling background images of houses. Also need to show a proposal date at the start of the document along with something that says 'This proposal is valid for 30 days'

```html
<!DOCTYPE html>
<html lang="en">
<head>
<meta charset="utf-8">
<title>Property Proposal – 8502 Lantana Ridge West, Hope Island QLD</title>
<link rel="stylesheet" href="https://fonts.googleapis.com/css2?family=Poppins:wght@300;400;500;600;700&display=swap">
<style>
:root{
  --navy:#15305f;
  --blue:#2463b4;
  --green:#5bb53b;
  --text:#2b2b2b;
  --muted:#555b63;
  --grey:#f2f4f3;
  --line:#d9dee4;
  --white:#ffffff;
}
*{box-sizing:border-box;margin:0;padding:0}
html,body{width:1200px;height:4962px;overflow:hidden}
body{position:relative;font-family:'Poppins',sans-serif;color:var(--text);background:var(--white);font-size:9.5px;line-height:1.5}
p{margin-bottom:9px}
.title{font-size:19px;font-weight:500;color:var(--blue);position:relative;padding-bottom:9px;line-height:1.2}
.title::after{content:"";position:absolute;left:0;bottom:0;width:46px;height:4px;background:var(--green);border-radius:2px}
.title.center{text-align:center}
.title.center::after{left:50%;transform:translateX(-50%)}
.abs{position:absolute}
.pill{display:inline-flex;align-items:center;gap:6px;border-radius:16px;font-size:10px;font-weight:600;letter-spacing:.4px;text-transform:uppercase}

/* header */
.brand{left:75px;top:22px;display:flex;flex-direction:column;align-items:center;width:90px}
.brand-mark{width:22px;height:22px;border-radius:50%;background:var(--blue)}
.brand-name{font-size:13px;font-weight:500;color:var(--navy);margin-top:3px}
.speak{left:996px;top:35px;width:127px;height:29px;border:1.5px solid var(--blue);color:var(--blue);justify-content:center}

/* hero */
.hero{left:75px;top:100px;width:1050px;height:405px;border-radius:0 0 22px 0;background:linear-gradient(180deg,#b9cddf 0%,#8aa7bf 35%,#6c6a62 62%,#3f4a3a 100%);text-align:center;color:var(--white)}
.hero-title{position:absolute;left:0;right:0;top:180px;font-size:24px;font-weight:600;text-shadow:0 1px 4px rgba(0,0,0,.35)}
.hero-title span{font-weight:400}
.hero-sub{position:absolute;left:0;right:0;top:216px;font-size:14px}
.hero-btn{position:absolute;left:470px;top:252px;width:110px;height:28px;background:var(--blue);color:var(--white);justify-content:center}

/* welcome */
.welcome{left:150px;top:603px;width:428px}
.welcome .title{margin-bottom:20px}
.signature{width:150px;height:34px;background:#eef1f6;border-radius:4px;margin-top:4px}
.agent{left:618px;top:562px;width:432px;height:361px;border-radius:4px;overflow:hidden}
.agent-photo{height:253px;background:linear-gradient(135deg,#e9edf0 0%,#cfd8e0 50%,#9fb0c2 100%)}
.agent-panel{height:108px;background:var(--navy);color:var(--white);padding:20px 20px 0}
.agent-name{font-size:19px;color:var(--green);font-weight:500}
.agent-name span{color:var(--white);font-weight:400}
.agent-contact{font-size:9px;margin-top:14px;line-height:1.7}
.agent-btn{position:absolute;right:27px;bottom:21px;width:131px;height:30px;background:var(--white);color:var(--blue);justify-content:center}

/* feature */
.feature{left:150px;top:978px;width:900px;height:405px;border-radius:12px;overflow:hidden;background:linear-gradient(180deg,#c7b8a4 0%,#a9573f 35%,#7e6a58 60%,#4aa3c4 80%,#2e8bb5 100%)}
.feature-box{position:absolute;left:0;top:270px;width:472px;height:112px;background:rgba(21,48,95,.88);color:var(--white);padding:18px 20px}
.feature-box h2{font-size:18px;font-weight:500;color:var(--green)}
.feature-box h2 span{color:var(--white);font-weight:400}
.specs{display:flex;align-items:center;gap:14px;margin-top:16px;font-size:10px}
.specs span{display:inline-flex;align-items:center;gap:6px}

/* listings */
.cards{left:150px;width:900px;display:grid;grid-template-columns:repeat(4,210px);column-gap:20px}
.card-img{height:156px;position:relative;border-radius:2px}
.badge{position:absolute;left:10px;top:10px;width:30px;height:30px;border-radius:50%;background:var(--blue);color:var(--white);font-size:6.5px;font-weight:600;display:flex;align-items:center;justify-content:center}
.card-addr{font-size:10.5px;color:var(--blue);margin-top:19px;line-height:1.35}
.card-sub{font-size:9.5px;color:var(--blue);text-transform:uppercase;line-height:1.4}
.card-specs{font-size:9px;margin:9px 0 5px;color:var(--text)}
.card-specs b{font-weight:600}
.card-row{font-size:9px;line-height:1.65}
.card-row b{font-weight:600}
.scrollbar{left:150px;width:900px;height:5px;background:#e2e5e8;border-radius:3px}
.scrollbar i{display:block;height:5px;background:#3b3f46;border-radius:3px}

/* trends */
.trends{left:150px;top:2238px;width:428px}
.trends .title{margin-bottom:20px}
.indicative{left:618px;top:2238px;width:432px}
.indicative .title{margin-bottom:20px}
.value-box{margin-top:20px;display:flex;height:89px}
.value-box div{flex:1;padding:16px 20px}
.value-box .range{background:var(--navy);color:var(--green)}
.value-box .offer{background:var(--green);color:var(--white)}
.value-box strong{display:block;font-size:19px;font-weight:500}
.value-box small{display:block;font-size:9px;margin-top:12px;color:var(--white)}

/* analysis */
.analysis-band{left:0;top:2587px;width:1200px;height:360px;background:var(--grey)}
.analysis{left:150px;top:2665px;width:428px}
.analysis .title{margin-bottom:20px}
.lead{font-size:11.5px;font-weight:500;line-height:1.5;margin-bottom:8px}
.analysis-img{left:618px;top:2643px;width:432px;height:246px;border-radius:2px;background:linear-gradient(180deg,#f3f3ef 0%,#dcdfd8 50%,#9aa88a 75%,#b89c78 100%)}

/* preparation */
.prep{left:150px;top:3000px;width:900px}
.prep .title{margin-bottom:20px}
.prep-grid{display:grid;grid-template-columns:repeat(3,290px);column-gap:7px;row-gap:7px;margin-top:10px}
.prep-item{height:121px;border:1px solid var(--line);border-radius:3px;padding:14px 14px 10px;display:flex;gap:12px}
.prep-item svg{flex:none}
.prep-item h3{font-size:9px;font-weight:500;margin-bottom:3px}
.prep-item p{font-size:8.5px;line-height:1.4;margin:0}

/* marketing */
.marketing-img{left:150px;top:3426px;width:430px;height:251px;border-radius:2px;background:linear-gradient(160deg,#e9e7e2 0%,#d8d2c8 40%,#8f6c4b 70%,#5a5c5c 100%)}
.marketing{left:618px;top:3448px;width:432px}
.marketing .title{margin-bottom:20px}

/* packages */
.packages-title{left:0;top:3732px;width:1200px}
.packages{left:312px;top:3775px;width:574px;height:362px;display:flex}
.package{flex:1;border:1px solid var(--line);position:relative}
.package-head{height:56px;padding:16px 18px;font-size:19px;color:var(--white)}
.package.one .package-head{background:var(--navy)}
.package.one .package-head b{color:var(--green);font-weight:500}
.package.two .package-head{background:var(--green)}
.package.two .package-head b{color:var(--navy);font-weight:500}
.package ul{list-style:none;padding:20px 18px 0}
.package li{display:flex;gap:9px;font-size:8.5px;line-height:1.35;margin-bottom:17px}
.package li b{font-weight:600;display:block}
.package li svg{flex:none;margin-top:1px}
.pkg-btn{position:absolute;left:48px;top:322px;width:192px;height:28px;background:var(--blue);color:var(--white);justify-content:center}
.options{left:0;top:4160px;width:1200px;text-align:center;font-size:11px}
.option-row{display:flex;justify-content:center;gap:22px;margin-top:12px;font-size:11px}
.option-row label{display:inline-flex;align-items:center;gap:8px}
.option-row i{width:14px;height:14px;border:1px solid #bfc5cc;display:inline-block}
.option-row b{font-weight:600}
.select-btn{left:553px;top:4232px;width:94px;height:26px;border:1.5px solid var(--blue);color:var(--blue);justify-content:center}

/* commission */
.commission{left:150px;top:4410px;width:430px}
.commission .title{margin-bottom:20px}
.commission-box{left:150px;top:4516px;width:430px;height:56px;border:1px solid #b9c0c8;border-radius:0 8px 8px 0;display:flex;align-items:center}
.rate{width:72px;height:100%;background:var(--navy);color:var(--white);font-size:19px;display:flex;align-items:center;justify-content:center}
.commission-box p{margin:0 0 0 14px;font-size:8.5px}
.commission-img{left:618px;top:4368px;width:432px;height:305px;border-radius:2px;background:linear-gradient(160deg,#8a7558 0%,#4f6b3e 40%,#b79c78 70%,#3b5a36 100%)}

/* footer */
.footer{left:0;top:4676px;width:1200px;height:135px;background:var(--navy)}
.copyright{position:absolute;left:150px;top:66px;color:var(--white);font-size:10px}
.copyright b{font-weight:600}
.social{position:absolute;top:63px;width:20px;height:20px;border:1.5px solid var(--white)}
.disclaimer{left:150px;top:4822px;width:900px;font-size:8.4px;line-height:1.45}
.disclaimer p{margin-bottom:8px}
.disclaimer b{font-weight:600}
</style>
</head>
<body>

<div class="abs brand"><span class="brand-mark"></span><span class="brand-name">Your Agency</span></div>
<a class="abs pill speak">Speak to us
  <svg width="9" height="9" viewBox="0 0 10 10"><path d="M2 8 8 2M3 2h5v5" stroke="currentColor" stroke-width="1.5" fill="none"/></svg></a>

<section class="abs hero" role="img" aria-label="Modern two-storey timber and concrete home at dusk">
  <h1 class="hero-title">Proposal for 8502 Lantana Ridge West <span>HOPE ISLAND QLD</span></h1>
  <p class="hero-sub">This proposal is valid for 30 days</p>
  <a class="pill hero-btn">Learn more</a>
</section>

<section class="abs welcome">
  <h2 class="title">Hello &amp; Welcome</h2>
  <p><b>Dear Marcus,</b></p>
  <p>Everyone likes to know what's happening in the property market in their suburb. One of the foundations of understanding your property's value is knowing what sale prices have recently been achieved.</p>
  <p>Knowledge is power and while there are multiple factors that play a role in determining current market value, surrounding sales provide valuable insight.</p>
  <p>Below we have listed some recent sales in the area to help you stay informed. If you're interested in a valuation update specific to your property, click the request button at the end of this report.</p>
  <p><b>Regards,</b></p>
  <div class="signature" role="img" aria-label="Handwritten signature of Oliver Brandt"></div>
</section>

<aside class="abs agent">
  <div class="agent-photo" role="img" aria-label="Portrait of the agent working at a laptop"></div>
  <div class="agent-panel">
    <div class="agent-name">Oliver Brandt <span>Your Agent</span></div>
    <div class="agent-contact">Mobile: <b>0412 785 316</b> &nbsp;&nbsp;&nbsp;&nbsp; Phone: <b>07 5530 1186</b><br>Email: <b>oliver@quillbrooktech.com.au</b></div>
  </div>
  <a class="pill agent-btn">Learn more
    <svg width="9" height="9" viewBox="0 0 10 10"><path d="M2 8 8 2M3 2h5v5" stroke="currentColor" stroke-width="1.5" fill="none"/></svg></a>
</aside>

<section class="abs feature" role="img" aria-label="Single-storey terracotta-roof home with courtyard pool">
  <div class="feature-box">
    <h2>8502 Lantana Ridge West <span>HOPE ISLAND QLD</span></h2>
    <div class="specs">
      <span><svg width="18" height="12" viewBox="0 0 18 12" fill="none" stroke="#fff" stroke-width="1.2"><path d="M1 11V1M1 7h16v4M4 7V4h6v3"/></svg>4</span>
      <span><svg width="16" height="13" viewBox="0 0 16 13" fill="none" stroke="#fff" stroke-width="1.2"><path d="M1 6h14v3a3 3 0 0 1-3 3H4a3 3 0 0 1-3-3zM3 6V2a1 1 0 0 1 2 0"/></svg>2</span>
      <span><svg width="18" height="12" viewBox="0 0 18 12" fill="none" stroke="#fff" stroke-width="1.2"><path d="M2 8l2-5h10l2 5v3H2zM5 11v1M13 11v1"/></svg>4</span>
      <span><svg width="14" height="14" viewBox="0 0 14 14" fill="none" stroke="#fff" stroke-width="1.2"><rect x="1" y="1" width="12" height="12"/><path d="M4 4h6v6"/></svg>1,674 Square Metres</span>
    </div>
  </div>
</section>

<h2 class="abs title center" style="left:0;top:1430px;width:1200px">Previous sales in your area</h2>
<div class="abs cards" style="top:1481px">
  <article>
    <div class="card-img" style="background:linear-gradient(180deg,#b9d2ea,#e7e6e1 55%,#7a8a72)" role="img" aria-label="White modern two-storey home"><span class="badge">SOLD</span></div>
    <div class="card-addr">12 Heron Bend</div><div class="card-sub">Boulevard Helensvale</div>
    <div class="card-specs">Bed <b>4</b> &nbsp;Bath <b>3</b> &nbsp;Garage <b>4</b></div>
    <div class="card-row">Sold for: &nbsp;&nbsp;<b>*$1,650,000</b><br>Sold on: &nbsp;&nbsp;<b>14/07/2025</b></div>
  </article>
  <article>
    <div class="card-img" style="background:linear-gradient(180deg,#c4d7e6,#7f9c8a 50%,#6b8a99)" role="img" aria-label="Aerial view of waterfront estate"><span class="badge">SOLD</span></div>
    <div class="card-addr">18 Kestrel Point</div><div class="card-sub">Helensvale</div>
    <div class="card-specs">Bed <b>4</b> &nbsp;Bath <b>2</b> &nbsp;Garage <b>3</b></div>
    <div class="card-row">Sold for: &nbsp;&nbsp;<b>$1,750,000</b><br>Sold on: &nbsp;&nbsp;<b>15/02/2025</b></div>
  </article>
  <article>
    <div class="card-img" style="background:linear-gradient(160deg,#5f7a4f,#a4573e 50%,#6e8055)" role="img" aria-label="Aerial view of home with red tiled roof"><span class="badge">SOLD</span></div>
    <div class="card-addr">2210 Bayside Parade</div><div class="card-sub">Hope Island</div>
    <div class="card-specs">Bed <b>4</b> &nbsp;Bath <b>3</b> &nbsp;Garage <b>2</b></div>
    <div class="card-row">Sold for: &nbsp;&nbsp;<b>$1,700,000</b><br>Sold on: &nbsp;&nbsp;<b>11/09/2024</b></div>
  </article>
  <article>
    <div class="card-img" style="background:linear-gradient(180deg,#cfe0ee,#5e8bb0 50%,#6f8a6a)" role="img" aria-label="Aerial view of canal estate"><span class="badge">SOLD</span></div>
    <div class="card-addr">31 Tidewater Close</div><div class="card-sub">Helensvale</div>
    <div class="card-specs">Bed <b>3</b> &nbsp;Bath <b>2</b> &nbsp;Garage <b>2</b></div>
    <div class="card-row">Sold for: &nbsp;&nbsp;<b>$1,600,000</b><br>Sold on: &nbsp;&nbsp;<b>23/01/2025</b></div>
  </article>
</div>
<div class="abs scrollbar" style="top:1780px"><i style="width:438px"></i></div>

<h2 class="abs title center" style="left:0;top:1831px;width:1200px">Properties on the market in your area</h2>
<div class="abs cards" style="top:1882px">
  <article>
    <div class="card-img" style="background:linear-gradient(180deg,#ecebe7,#c9c3b8 60%,#8d7a64)" role="img" aria-label="Open-plan living and kitchen interior"><span class="badge">LISTED</span></div>
    <div class="card-addr">18 Kestrel Point</div><div class="card-sub">Helensvale QLD</div>
    <div class="card-specs">Bed <b>4</b> &nbsp;Bath <b>2</b> &nbsp;Garage <b>3</b></div>
    <div class="card-row">Listed for: &nbsp;&nbsp;<b>Contact Agent</b><br>Listed on: &nbsp;&nbsp;<b>07/01/2025</b></div>
  </article>
  <article>
    <div class="card-img" style="background:linear-gradient(180deg,#b7cde0,#4a5560 45%,#6c8a5a)" role="img" aria-label="Aerial view of home with dark roof"><span class="badge">LISTED</span></div>
    <div class="card-addr">6 Ketchside Court</div><div class="card-sub">Helensvale QLD</div>
    <div class="card-specs">Bed <b>4</b> &nbsp;Bath <b>3</b> &nbsp;Garage <b>2</b></div>
    <div class="card-row">Listed for: &nbsp;&nbsp;<b>Expressions of Interest</b><br>Listed on: &nbsp;&nbsp;<b>14/01/2025</b></div>
  </article>
  <article>
    <div class="card-img" style="background:linear-gradient(180deg,#5b7fa8,#c3a58a 45%,#3fa4d1)" role="img" aria-label="Home at dusk with lit pool"><span class="badge">LISTED</span></div>
    <div class="card-addr">44 Ashford Grove Drive</div><div class="card-sub">Helensvale QLD</div>
    <div class="card-specs">Bed <b>4</b> &nbsp;Bath <b>2</b> &nbsp;Garage <b>2</b></div>
    <div class="card-row">Listed for: &nbsp;&nbsp;<b>Just Listed! Water Views!<br>&nbsp;&nbsp;&nbsp;&nbsp;&nbsp;&nbsp;&nbsp;&nbsp;&nbsp;&nbsp;&nbsp;&nbsp;&nbsp;&nbsp;&nbsp;&nbsp;&nbsp;&nbsp;Side Access!</b><br>Listed on: &nbsp;&nbsp;<b>11/09/2025</b></div>
  </article>
  <article>
    <div class="card-img" style="background:linear-gradient(180deg,#4f86c6,#e3e3df 45%,#2fa3cf)" role="img" aria-label="Modern home with pool under blue sky"><span class="badge">LISTED</span></div>
    <div class="card-addr">417 Pelican Reach Promenade</div><div class="card-sub">Helensvale QLD</div>
    <div class="card-specs">Bed <b>4</b> &nbsp;Bath <b>2</b> &nbsp;Garage <b>3</b></div>
    <div class="card-row">Listed for: &nbsp;&nbsp;<b>Offers Over $1.65mil</b><br>Listed on: &nbsp;&nbsp;<b>18/06/2025</b></div>
  </article>
</div>
<div class="abs scrollbar" style="top:2178px"><i style="width:210px"></i></div>

<section class="abs trends">
  <h2 class="title">Current Market Trends</h2>
  <p>Hope Island's real estate market continues to demonstrate strong resilience, particularly in its premium waterfront and lifestyle segments. According to ValuMetric data via Property Ledger Magazine, the current median house price stands at approximately AUD1.85 million, with an annual capital growth rate of 0.00%, and houses now spend an average of 57 days on market.</p>
  <p>Rental yields hold steady at around 3.72%, supported by a median weekly rent of AUD1,150. Notably, while quarterly house values have declined by about −3.65%, the 12-month trend remains flat, reflecting a stable yet cautious market environment.</p>
  <p>In contrast, units have become a standout performer in the Hope Island market. Homefinder.com.au reports that units have posted a robust 7.2% annual growth rate, with median sale prices around AUD 879,000, and rental yields averaging 4.7%—above the house segment. Monthly data reveals that units offer compelling demand: growing median rental prices, shrinking vacancy periods, and strong investor interest.</p>
  <p>Meanwhile, local historic trends show that well-located 4- and 5-bedroom houses continue to command a premium, with median prices ranging from AUD 2 million for 4 beds to AUD 2.77 million for 5-beds, both segments showing double-digit year-on-year growth—11.9% and 19.1% respectively.</p>
</section>
<section class="abs indicative">
  <h2 class="title">Indicative Value</h2>
  <p class="lead">Reviewing what similar properties have recently sold along with those that are currently on the market, we estimate the below price range will be achieved for your property.</p>
  <div class="value-box">
    <div class="range"><strong>$1.5 M to $1.8 M</strong><small>Indicative Value</small></div>
    <div class="offer"><strong>Offers over $1.6 M</strong><small>Recommended List Price</small></div>
  </div>
</section>

<div class="abs analysis-band"></div>
<section class="abs analysis">
  <h2 class="title">Property Analysis</h2>
  <p class="lead">This Price Update is perfect for monitoring the market, however we are able to provide a current market valuation for your property if you're interested. This can be done in two ways:</p>
  <p>An e-Update which can be emailed to you, however please bear in mind that this will not be validated by an on-site viewing of the property.</p>
  <p>Alternatively, we can meet at the property to do a full assessment and provide you with a valuation taking into account the location, views, presentation and condition of your property along with recent sales of local homes and our in depth market knowledge.</p>
</section>
<div class="abs analysis-img" role="img" aria-label="Bright living room opening onto garden views"></div>

<section class="abs prep">
  <h2 class="title">Preparation</h2>
  <p>To maximise buyer interest and achieve the strongest possible sale price, we recommend a strategic approach to preparing your property for market. Presentation plays a critical role in attracting premium buyers—particularly in Hope Island, where lifestyle appeal and first impressions are paramount.</p>
  <div class="prep-grid">
    <div class="prep-item">
      <svg width="44" height="44" viewBox="0 0 44 44" fill="none" stroke="var(--navy)" stroke-width="1.4"><path d="M12 14h20M15 14l2 24h10l2-24M18 14v-4h8v4M20 19v14M24 19v14"/></svg>
      <div><h3>Declutter and Depersonalise</h3><p>Remove excess personal items and streamline furniture to create a sense of space and allow buyers to visualise themselves in the property.</p></div>
    </div>
    <div class="prep-item">
      <svg width="44" height="44" viewBox="0 0 44 44" fill="none" stroke="var(--navy)" stroke-width="1.4"><rect x="8" y="8" width="14" height="10"/><path d="M15 18v20M10 38h10M26 22h12v8H26zM28 30v8M36 30v8"/></svg>
      <div><h3>Professional Styling</h3><p>Engage a home stylist to highlight your property's best features, with furniture, artwork and décor selected to appeal to the target market.</p></div>
    </div>
    <div class="prep-item">
      <svg width="44" height="44" viewBox="0 0 44 44" fill="none" stroke="var(--navy)" stroke-width="1.4"><path d="M6 22 22 8l16 14M10 19v19h24V19"/><path d="M17 33l12-12M27 19l4 4" stroke="var(--green)"/></svg>
      <div><h3>Minor Repairs &amp; Maintenance</h3><p>Address any visible wear and tear, such as paint touch-ups, leaking taps, cracked tiles or weathered timber, to ensure the property presents as well-maintained.</p></div>
    </div>
    <div class="prep-item">
      <svg width="44" height="44" viewBox="0 0 44 44" fill="none" stroke="var(--navy)" stroke-width="1.4"><circle cx="16" cy="14" r="7" stroke="var(--green)"/><path d="M16 21v10M4 32c8-3 28-3 36 0M4 38c8-3 28-3 36 0"/></svg>
      <div><h3>Landscaping and Street Appeal</h3><p>Invest in fresh mulch, trimmed hedges, mowed lawns, and seasonal flowers to create an inviting entrance. Waterfront properties should ensure pontoons, boardwalks and outdoor living areas are presented in excellent condition.</p></div>
    </div>
    <div class="prep-item">
      <svg width="44" height="44" viewBox="0 0 44 44" fill="none" stroke="var(--navy)" stroke-width="1.4"><path d="M14 18h10v20H14zM16 18v-5h6v5M24 22h6M8 10l2 2M12 6v3M6 16h3"/><path d="M30 28h8v10h-8z" stroke="var(--green)"/></svg>
      <div><h3>Deep Cleaning</h3><p>Engage professional cleaners to ensure all surfaces, windows, carpets and outdoor areas are spotless before photography and open homes.</p></div>
    </div>
    <div class="prep-item">
      <svg width="44" height="44" viewBox="0 0 44 44" fill="none" stroke="var(--navy)" stroke-width="1.4"><rect x="8" y="6" width="28" height="32"/><path d="M12 12h8v8h-8zM24 12h8M24 16h8M12 26h20M12 31h20"/><circle cx="16" cy="16" r="2" stroke="var(--green)"/></svg>
      <div><h3>High-Quality Marketing Preparation</h3><p>Allow time for professional photography, drone footage, floor plans, and potentially twilight photography to showcase the property in its most appealing light.</p></div>
    </div>
  </div>
  <p style="margin-top:12px">By following these recommendations, we position your property to stand out in the competitive Hope Island market, attract more qualified buyers, and create the conditions for a strong sale result.</p>
</section>

<div class="abs marketing-img" role="img" aria-label="Contemporary kitchen with timber island and white cabinetry"></div>
<section class="abs marketing">
  <h2 class="title">Marketing Strategy</h2>
  <p class="lead">Your listing will rotate back to the top of the first page of search results every 15 days. This exposes your listing to more and newer buyers continually.</p>
  <p>With over half of Queenslanders not going past the first page of search results, you'll be seen ahead of almost three quarters of the listings in QLD and give your listing a better chance to get on page one.</p>
  <p>Give buyers a taste of why they should choose your property. Your review will sit below the property description and provide a unique insight into the local area. Community content like this has attracted more than 7.4M buyers to the site since launching This exclusive tool can promote your home in a way that no other portal can.</p>
</section>

<h2 class="abs title center packages-title">Please select a package below.</h2>
<div class="abs packages">
  <div class="package one">
    <div class="package-head">Package 1 <b>$503.20</b></div>
    <ul>
      <li><svg width="13" height="13" viewBox="0 0 13 13"><circle cx="6.5" cy="6.5" r="5.8" fill="none" stroke="var(--green)"/><path d="M3.8 6.7l1.9 1.9 3.6-3.8" fill="none" stroke="var(--green)" stroke-width="1.3"/></svg><span><b>Major website</b>homefinder.com.au (premier Plus)<br>propertylane.com.au (Silver) nestly.com.au<br>(Silver)</span></li>
      <li><svg width="13" height="13" viewBox="0 0 13 13"><circle cx="6.5" cy="6.5" r="5.8" fill="none" stroke="var(--green)"/><path d="M3.8 6.7l1.9 1.9 3.6-3.8" fill="none" stroke="var(--green)" stroke-width="1.3"/></svg><span><b>Minor websites</b>ruralvista.com.au,<br>keystonecommercial.com.au</span></li>
      <li><svg width="13" height="13" viewBox="0 0 13 13"><circle cx="6.5" cy="6.5" r="5.8" fill="none" stroke="var(--green)"/><path d="M3.8 6.7l1.9 1.9 3.6-3.8" fill="none" stroke="var(--green)" stroke-width="1.3"/></svg><span><b>Property Ebook</b></span></li>
      <li><svg width="13" height="13" viewBox="0 0 13 13"><circle cx="6.5" cy="6.5" r="5.8" fill="none" stroke="var(--green)"/><path d="M3.8 6.7l1.9 1.9 3.6-3.8" fill="none" stroke="var(--green)" stroke-width="1.3"/></svg><span><b>Professional Photography Package</b>Photos, Video, Drone and Floorplan</span></li>
      <li><svg width="13" height="13" viewBox="0 0 13 13"><circle cx="6.5" cy="6.5" r="5.8" fill="none" stroke="var(--green)"/><path d="M3.8 6.7l1.9 1.9 3.6-3.8" fill="none" stroke="var(--green)" stroke-width="1.3"/></svg><span><b>Signboard</b></span></li>
    </ul>
    <a class="pill pkg-btn">Select your package
      <svg width="10" height="9" viewBox="0 0 10 9"><path d="M1 4.5h8M5.5 1l3.5 3.5L5.5 8" fill="none" stroke="#fff" stroke-width="1.3"/></svg></a>
  </div>
  <div class="package two">
    <div class="package-head">Package 2 <b>$3,000</b></div>
    <ul>
      <li><svg width="13" height="13" viewBox="0 0 13 13"><circle cx="6.5" cy="6.5" r="5.8" fill="none" stroke="var(--green)"/><path d="M3.8 6.7l1.9 1.9 3.6-3.8" fill="none" stroke="var(--green)" stroke-width="1.3"/></svg><span><b>Major website</b>homefinder.com.au (premier Plus)<br>propertylane.com.au (Silver) nestly.com.au<br>(Silver)</span></li>
      <li><svg width="13" height="13" viewBox="0 0 13 13"><circle cx="6.5" cy="6.5" r="5.8" fill="none" stroke="var(--green)"/><path d="M3.8 6.7l1.9 1.9 3.6-3.8" fill="none" stroke="var(--green)" stroke-width="1.3"/></svg><span><b>Minor websites</b>listwise.com.au,<br>harbourlinepartners.com</span></li>
      <li><svg width="13" height="13" viewBox="0 0 13 13"><circle cx="6.5" cy="6.5" r="5.8" fill="none" stroke="var(--green)"/><path d="M3.8 6.7l1.9 1.9 3.6-3.8" fill="none" stroke="var(--green)" stroke-width="1.3"/></svg><span><b>Property Ebook</b></span></li>
      <li><svg width="13" height="13" viewBox="0 0 13 13"><circle cx="6.5" cy="6.5" r="5.8" fill="none" stroke="var(--green)"/><path d="M3.8 6.7l1.9 1.9 3.6-3.8" fill="none" stroke="var(--green)" stroke-width="1.3"/></svg><span><b>Professional Photography Package</b>Photos, Video, Drone and Floorplan</span></li>
      <li><svg width="13" height="13" viewBox="0 0 13 13"><circle cx="6.5" cy="6.5" r="5.8" fill="none" stroke="var(--green)"/><path d="M3.8 6.7l1.9 1.9 3.6-3.8" fill="none" stroke="var(--green)" stroke-width="1.3"/></svg><span><b>Signboard</b></span></li>
    </ul>
    <a class="pill pkg-btn">Select your package
      <svg width="10" height="9" viewBox="0 0 10 9"><path d="M1 4.5h8M5.5 1l3.5 3.5L5.5 8" fill="none" stroke="#fff" stroke-width="1.3"/></svg></a>
  </div>
</div>
<div class="abs options">
  <p style="margin:0">Please select any of the following options you would like to be included in your marketing campaign:</p>
  <div class="option-row">
    <label><i></i>Sign board <b>$150</b></label>
    <label><i></i>Mail Out <b>$140</b></label>
    <label><i></i>Done photography <b>$550</b></label>
  </div>
</div>
<a class="abs pill select-btn">Select
  <svg width="10" height="9" viewBox="0 0 10 9"><path d="M1 4.5h8M5.5 1l3.5 3.5L5.5 8" fill="none" stroke="currentColor" stroke-width="1.3"/></svg></a>

<section class="abs commission">
  <h2 class="title">Commission Structure</h2>
  <p class="lead">Portal costs are based on your location and the density of the area, the portal calculates this cost. We pass this directly on to you with no add-on costs.</p>
</section>
<div class="abs commission-box"><div class="rate">4.3 %</div><p>* commission quoted is inclusive GST</p></div>
<div class="abs commission-img" role="img" aria-label="Aerial view of a leafy suburban neighbourhood"></div>

<footer class="abs footer">
  <p class="copyright">© 2025 <b>Your Agency Realtors</b> - All rights reserved</p>
  <span class="social" style="left:999px"></span>
  <span class="social" style="left:1029px"></span>
</footer>
<div class="abs disclaimer">
  <p><b>Disclaimer:</b> The information displayed in this document may be based on historical and current data supplied to ListData Pty Ltd by third parties including State government agencies and constitutes "Third Party Data" or "Third Party Information". ListData does not make any warranty as to the accuracy, completeness or reliability of the information or accept any liability arising in any way from any omissions or errors in this information. The information should not be regarded as advice or relied upon by you or any other person and ListData recommend that you seek professional advice before making any property decisions.</p>
  <p>Based on or contains data provided by the State Land Records Office 2017. In consideration of the State permitting the use of this data you acknowledge and agree that the State gives no warranty in relation to the data (including accuracy, reliability, completeness, currency or suitability) and accepts no liability (including without limitation, liability in negligence) for any loss, damage or costs (including consequential damage) relating to any use of the data. Data must not be used for direct marketing or be used in breach of privacy laws.</p>
</div>

</body>
</html>
```